We are having a Bright Dawn, Bold Self Reshape Challenge at our fitness studio. We need a poster design using the template attached as a reference. I have also included our Vorabloom logo to put on the poster. Please DO NOT use the graphics in the flyer as we are expecting something much better :-)

-Size needed 11x17 with bleeding for printing

-We need this made in Photoshop (CS3 friendly) or at least delivered in PS as we might change some text or re-arrange the design later on.

-We need this in layers.

```html
<!DOCTYPE html>
<html lang="en">
<head>
<meta charset="utf-8">
<title>Vorabloom Bootcamps – Bright Dawn, Bold Self Reshape Challenge</title>
<link rel="stylesheet" href="https://fonts.googleapis.com/css2?family=Fira+Sans:wght@300;500;600;800&family=Open+Sans:wght@600;700;800&display=swap">
<style>
  :root {
    --bg-deep: #131619;
    --bg-mid: #343c42;
    --bg-glow: #56606a;
    --skin-light: #b08466;
    --skin: #8d644c;
    --skin-shade: #5a3f31;
    --trousers: #1a1c1f;
    --accent-red: #e8141b;
    --paper: #ffffff;
    --plate: #e9e9e6;
    --ink-dark: #2a2d30;
    --line: #e6e6e6;
  }
  * { margin: 0; padding: 0; box-sizing: border-box; }
  html, body { width: 782px; height: 1200px; overflow: hidden; background: var(--bg-deep); }
  .poster {
    position: relative;
    width: 782px;
    height: 1200px;
    overflow: hidden;
    font-family: "Fira Sans", sans-serif;
    color: var(--paper);
  }
  .backdrop {
    position: absolute; inset: 0;
    background:
      radial-gradient(ellipse 70% 50% at 50% 55%, var(--bg-glow) 0%, var(--bg-mid) 45%, var(--bg-deep) 100%);
  }
  .athlete-photo {
    position: absolute;
    left: 250px; top: 70px; width: 532px; height: 1130px;
    background:
      linear-gradient(90deg, var(--bg-mid) 0%, rgba(52,60,66,0) 22%, rgba(52,60,66,0) 88%, rgba(19,22,25,0.7) 100%),
      linear-gradient(180deg,
        rgba(52,60,66,0) 0%,
        var(--skin-shade) 8%,
        var(--skin) 22%,
        var(--skin-light) 38%,
        var(--skin) 55%,
        var(--skin-shade) 66%,
        var(--trousers) 74%,
        var(--trousers) 100%);
    -webkit-mask-image: radial-gradient(ellipse 62% 70% at 62% 50%, #000 55%, transparent 100%);
    mask-image: radial-gradient(ellipse 62% 70% at 62% 50%, #000 55%, transparent 100%);
  }
  .brand-plate {
    position: absolute;
    left: 50px; top: 38px; width: 420px; height: 156px;
    background: var(--plate);
    border: 4px solid var(--ink-dark);
    border-radius: 6px;
    display: flex; flex-direction: column; align-items: center; justify-content: center;
    gap: 14px;
    color: var(--ink-dark);
    font-family: "Fira Sans", sans-serif;
    font-weight: 800;
  }
  .brand-name { font-size: 44px; line-height: 1; text-align: center; letter-spacing: 1px; }
  .brand-tagline { font-size: 15px; letter-spacing: 2px; }
  .schedule {
    position: absolute;
    left: 30px; top: 228px; width: 460px;
    text-align: center;
    font-weight: 500;
    font-size: 20px;
    line-height: 25.4px;
    white-space: nowrap;
  }
  .highlight { background: var(--accent-red); padding: 0 3px; }
  .quote-mark {
    position: absolute;
    color: var(--accent-red);
    font-family: "Fira Sans", sans-serif;
    font-weight: 800;
    font-size: 48px;
    line-height: 1;
  }
  .quote-open { left: 36px; top: 216px; }
  .quote-close { left: 408px; top: 344px; }
  .connectors { position: absolute; left: 0; top: 0; }
  .bubble {
    position: absolute;
    background: var(--paper);
    border-radius: 50%;
    color: var(--accent-red);
    font-family: "Open Sans", sans-serif;
    font-weight: 700;
    display: flex; flex-direction: column; align-items: center; justify-content: center;
    text-align: center;
    white-space: nowrap;
  }
  .bubble-title { left: 66px; top: 388px; width: 238px; height: 216px; font-size: 23px; line-height: 30px; }
  .bubble-title .lead { font-size: 27px; line-height: 36px; font-weight: 800; letter-spacing: -0.5px; }
  .bubble-prize { left: 58px; top: 616px; width: 144px; height: 158px; font-size: 18px; line-height: 25px; font-weight: 600; }
  .bubble-prize .amount { font-size: 42px; line-height: 46px; font-weight: 800; }
  .bubble-offer { left: 66px; top: 810px; width: 215px; height: 240px; font-size: 18px; line-height: 25.5px; font-weight: 600; padding-top: 6px; }
  .bubble-offer .price { font-size: 54px; line-height: 56px; font-weight: 800; }
  .more-info {
    position: absolute;
    left: 45px; top: 1098px;
    font-weight: 300;
    font-size: 24px;
    line-height: 31px;
  }
</style>
</head>
<body>
<main class="poster">
  <div class="backdrop"></div>
  <div class="athlete-photo" role="img" aria-label="Studio photo of a shirtless athlete in dark trousers holding a dumbbell, filling the right side of the poster"></div>

  <header class="brand-plate">
    <div class="brand-name">VORABLOOM<br>BOOTCAMPS</div>
    <div class="brand-tagline">THE ULTIMATE FITNESS SOLUTION</div>
  </header>

  <span class="quote-mark quote-open">&ldquo;</span>
  <section class="schedule">
    <p>In Just <span class="highlight">6 Weeks,</span> Transform Your Body And</p>
    <p>Get In The Best Shape Of Your Life!</p>
    <p>Kick Off Meeting: Thursday, <span class="highlight">Jan 14 at 7:30 pm</span></p>
    <p><span class="highlight">Start Date</span>: Monday, <span class="highlight">January 18th</span></p>
    <p><span class="highlight">End Date</span>: Friday, <span class="highlight">February 26th</span></p>
  </section>
  <span class="quote-mark quote-close">&rdquo;</span>

  <svg class="connectors" width="782" height="1200" viewBox="0 0 782 1200" aria-hidden="true">
    <g stroke="var(--line)" stroke-width="1.5" fill="none">
      <line x1="156" y1="602" x2="138" y2="618"/>
      <line x1="226" y1="600" x2="228" y2="698"/>
      <line x1="228" y1="698" x2="194" y2="812"/>
      <line x1="138" y1="772" x2="146" y2="812"/>
    </g>
    <circle cx="228" cy="698" r="7" fill="var(--paper)"/>
  </svg>

  <div class="bubble bubble-title">
    <span class="lead">BRIGHT DAWN</span>
    <span>BOLD SELF</span>
    <span>RESHAPE</span>
    <span>CHALLENGE</span>
  </div>

  <div class="bubble bubble-prize">
    <span class="amount">$500</span>
    <span>CASH Prize</span>
    <span>for Winner!</span>
  </div>

  <div class="bubble bubble-offer">
    <span>6 Weeks</span>
    <span>of Training,</span>
    <span>Nutrition,</span>
    <span>and Coaching</span>
    <span>Starting</span>
    <span>at just</span>
    <span class="price">$99!</span>
  </div>

  <footer class="more-info">
    <p>FOR MORE INFO</p>
    <p>Visit www.vorabloombootcamps.com</p>
  </footer>
</main>
</body>
</html>
```